Eyecatching Carpentry Business card

I need a business card designed for myself, my company name is Lewis Dunmore Carpentry.
I am based on the south coast of England and I do all aspects of carpentry, including;
skirting
Architraves
kitchens
roof construction
flooring
doors
loft conversions
decking
windows
I currently have no company logo or letter head so I leave all design ideas to designers.
All I ask is that it looks professional and modern.
A logo may be incorporated as well.
My contact details should be on the back, telephone and email.

```html
<!DOCTYPE html>
<html lang="en">
<head>
<meta charset="utf-8">
<title>Lewis Dunmore Carpentry – Business Card</title>
<link rel="stylesheet" href="https://fonts.googleapis.com/css2?family=Open+Sans:wght@400;600&display=swap">
<style>
  :root {
    --canvas-bg: #e9e6e2;
    --card-white: #ffffff;
    --wood-dark: #5e1a0e;
    --wood-mid: #8a3318;
    --wood-light: #a8481f;
    --ink: #1c1c1c;
    --tool-tone: #d9a62a;
    --tool-steel: #9ea3a8;
    --faint-tone: #f3ede0;
    --card-shadow: 0 10px 28px rgba(0,0,0,0.22);
  }
  * { box-sizing: border-box; margin: 0; padding: 0; }
  html, body {
    width: 1200px; height: 918px; overflow: hidden;
    background: var(--canvas-bg);
  }
  .canvas { position: relative; width: 1200px; height: 918px; }
  .card {
    position: absolute;
    background: var(--card-white);
    box-shadow: var(--card-shadow);
    overflow: hidden;
  }

  /* Front */
  .card-front { left: 130px; top: 299px; width: 560px; height: 320px; }
  .wood-band {
    position: absolute; left: 0; width: 100%;
    background: linear-gradient(90deg, var(--wood-dark), var(--wood-mid) 45%, var(--wood-light) 75%, var(--wood-mid));
  }
  .wood-band--top { top: 0; height: 56px; }
  .wood-band--bottom { bottom: 0; height: 64px; }
  .tool-emblem {
    position: absolute; left: 290px; top: 86px; width: 110px; height: 96px;
    border-radius: 6px;
    background: linear-gradient(135deg, var(--tool-steel), var(--tool-tone));
    opacity: 0.85;
  }
  .brand-name {
    position: absolute; left: 0; right: 0; top: 200px;
    text-align: center;
    font-family: "Open Sans", sans-serif;
    font-weight: 600;
    font-size: 30px;
    letter-spacing: 0.5px;
    line-height: 1.2;
    color: var(--ink);
    white-space: nowrap;
  }

  /* Back */
  .card-back { left: 750px; top: 179px; width: 320px; height: 560px; }
  .back-decor {
    position: absolute; left: 70px; top: 290px; width: 180px; height: 180px;
    border-radius: 8px;
    background: var(--faint-tone);
  }
  .contact {
    position: absolute; left: 34px; top: 40px;
    font-family: "Open Sans", sans-serif;
    color: var(--ink);
  }
  .contact__name { font-size: 26px; font-weight: 600; line-height: 1.1; }
  .contact__title { font-size: 14px; margin-bottom: 22px; }
  .contact__address { font-size: 16px; line-height: 1.3; margin-bottom: 18px; }
  .contact__phone { font-size: 16px; margin-bottom: 22px; }
  .contact__email { font-size: 16px; }
</style>
</head>
<body>
<main class="canvas">
  <section class="card card-front" aria-label="Card front">
    <div class="wood-band wood-band--top" role="img" aria-label="Dark red wood grain band"></div>
    <div class="tool-emblem" role="img" aria-label="Crossed hammer and hand saw illustration"></div>
    <h1 class="brand-name">Lewis Dunmore Carpentry</h1>
    <div class="wood-band wood-band--bottom" role="img" aria-label="Red wood grain band"></div>
  </section>

  <section class="card card-back" aria-label="Card back">
    <div class="back-decor" role="img" aria-label="Faint crossed hammer and saw illustration"></div>
    <div class="contact">
      <p class="contact__name">Your Name</p>
      <p class="contact__title">Your Title</p>
      <p class="contact__address">Sample Address<br>Sample Street</p>
      <p class="contact__phone">123456789</p>
      <p class="contact__email">sample@sample.com</p>
    </div>
  </section>
</main>
</body>
</html>
```